Brindle Advisory Business Card Design

Business card for business consulting company, using attached logo. We do financial and strategic consulting, and want a clean, professional image with a bit of fun. Our logo is a flat whale tail, which symbolizes the Orca whale, a highly collaborative, group based animal that is very successful in navigating the ocean, protecting the herd, and hunting. We like the logo that is blue and gray on white one one side, but would be open to a blue card with white lettering on the other side... or whatever you'd suggest
Updates
Hi all - I have had the logo modified to take the shadowing off the tail. I will post it on the brief... under a file name called updated logo. thank you Added Saturday, April 25, 2015
Target Market(s)
Small to medium sized businesses ($10M to $500M in revenue per year), financial and sales executives, general managers, attorneys and CPAs
Industry/Entity Type
Financial
Contact Information for Business Card
Want company name, contact info - name, title, telephone, email, website, linkedin, twitter and Facebook. No physical address yet.
Requirements
Must have
- contemporary design, bold, strong, confident but with a bit of fun. prominently feature the logo and the whale tail icon
Nice to have
- unique touches that would differentiate us from a regular card... for example, logo and writing all on front on white background, but on back - logo in white on a blue background
- open to idea of different shapes of card than standard... but not sure
Should not have
- ?

```html
<!DOCTYPE html>
<html lang="en">
<head>
<meta charset="utf-8">
<title>Brindle Advisory – Business Card</title>
<link rel="stylesheet" href="https://fonts.googleapis.com/css2?family=Open+Sans:wght@400;600;700&display=swap">
<style>
  :root {
    --stage: #9a9a9a;
    --paper: #ffffff;
    --navy: #17375f;
    --navy-soft: #1f3d66;
    --grey-text: #a3a3a3;
    --rule: #555b63;
    --white: #ffffff;
  }
  * { margin: 0; padding: 0; box-sizing: border-box; }
  html, body { width: 1200px; height: 900px; overflow: hidden; }
  body {
    background: var(--stage);
    font-family: "Open Sans", Arial, sans-serif;
    position: relative;
  }
  .card {
    position: absolute;
    left: 285px;
    width: 629px;
    height: 360px;
    overflow: hidden;
  }
  .card--front { top: 74px; background: var(--paper); }
  .card--back { top: 465px; background: var(--navy); }

  /* Front */
  .brand {
    position: absolute;
    left: 67px;
    top: 114px;
    display: flex;
    align-items: center;
    gap: 9px;
  }
  .brand__square {
    width: 40px; height: 40px;
    background: var(--navy);
    border-radius: 4px;
  }
  .brand__name {
    font-size: 30px;
    font-weight: 600;
    color: var(--navy);
    letter-spacing: -0.5px;
    line-height: 1;
  }
  .brand__tagline {
    position: absolute;
    left: 183px;
    top: 146px;
    font-size: 8px;
    font-weight: 600;
    color: var(--navy);
    letter-spacing: 0.2px;
  }
  .person__name {
    position: absolute;
    right: 59px;
    top: 133px;
    font-size: 21px;
    font-weight: 700;
    color: var(--navy);
    letter-spacing: 0.5px;
  }
  .divider {
    position: absolute;
    left: 67px;
    top: 166px;
    width: 503px;
    height: 1px;
    background: var(--rule);
  }
  .person__title {
    position: absolute;
    right: 57px;
    top: 170px;
    font-size: 13px;
    font-weight: 400;
    color: var(--grey-text);
    letter-spacing: 3px;
  }
  .contacts {
    position: absolute;
    left: 48px;
    top: 198px;
    list-style: none;
  }
  .contacts li {
    display: flex;
    align-items: center;
    height: 26px;
    font-size: 13px;
    color: var(--grey-text);
    letter-spacing: -0.2px;
  }
  .contacts svg { width: 18px; height: 18px; margin-right: 7px; flex: none; }

  /* Back */
  .back__wash {
    position: absolute;
    left: -120px;
    top: 20px;
    width: 420px;
    height: 420px;
    border-radius: 50%;
    background: var(--navy-soft);
  }
  .back__brand {
    position: absolute;
    left: 0; right: 0;
    top: 160px;
    display: flex;
    justify-content: center;
    align-items: center;
    gap: 10px;
  }
  .back__square { width: 30px; height: 30px; background: var(--white); border-radius: 3px; }
  .back__name {
    font-size: 28px;
    font-weight: 600;
    color: var(--white);
    letter-spacing: -0.3px;
  }
  .back__web {
    position: absolute;
    left: 0; right: 0;
    top: 327px;
    text-align: center;
    font-size: 13px;
    color: var(--white);
    letter-spacing: 5px;
  }
</style>
</head>
<body>
  <section class="card card--front">
    <div class="brand">
      <span class="brand__square"></span>
      <span class="brand__name">Brindle Advisory</span>
    </div>
    <span class="brand__tagline">business consulting</span>
    <p class="person__name">XXXXXXX</p>
    <div class="divider"></div>
    <p class="person__title">PRESIDENT</p>

    <ul class="contacts">
      <li>
        <svg viewBox="0 0 18 18" aria-hidden="true"><path fill="#17375f" d="M4 2 L7 2 L8 6 L6 7.5 Q7.5 11 10.5 12 L12 10 L16 11 L16 14 Q15 16 12.5 16 Q4 14 2 5 Q2 2.5 4 2 Z"/></svg>
        xxx xxx xxxx
      </li>
      <li>
        <svg viewBox="0 0 18 18" aria-hidden="true"><rect x="1" y="1" width="16" height="16" rx="3" fill="#17375f"/></svg>
        xxx xxx xxxx
      </li>
      <li>
        <svg viewBox="0 0 18 18" aria-hidden="true"><rect x="1" y="4" width="16" height="10" fill="#17375f"/><path d="M1.5 4.5 L9 10 L16.5 4.5" stroke="#fff" stroke-width="1.2" fill="none"/></svg>
        xxxxx@xxxxxx.com
      </li>
      <li>
        <svg viewBox="0 0 18 18" aria-hidden="true"><g fill="none" stroke="#17375f" stroke-width="1.4"><circle cx="9" cy="9" r="7.5"/><ellipse cx="9" cy="9" rx="3.2" ry="7.5"/><line x1="1.5" y1="9" x2="16.5" y2="9"/><line x1="3" y1="5" x2="15" y2="5"/><line x1="3" y1="13" x2="15" y2="13"/></g></svg>
        www.xxxxxxxx.com
      </li>
      <li>
        <svg viewBox="0 0 18 18" aria-hidden="true"><rect x="1" y="1" width="16" height="16" rx="2" fill="#17375f"/></svg>
        xxx xxx xxxx
      </li>
    </ul>
  </section>

  <section class="card card--back">
    <div class="back__wash" aria-hidden="true"></div>
    <div class="back__brand">
      <span class="back__square"></span>
      <span class="back__name">Brindle Advisory</span>
    </div>
    <p class="back__web">www.xxxxxxxx.com</p>
  </section>
</body>
</html>
```